Facebook Ad For New online Spectacle Store

We have started a new online store in Australia selling spectacles. As we don't have overheads such as rent electricity etc we are able to do these glasses at an extremely cheap price of $50 for the complete pair. We want to highlight the affordability and quality. This ad will be promoted on Facebook all over Australia. We want to make an impression. There are a lot of people wearing cheap magnifiers from chemists etc that are not suitable as most people need a corrective lens and rarely are both eyes the same power. So it's the people that are buying the $10 glasses we really want to sway to get ones that actually are the correct prescription for them without paying hundreds of dollars on a pair. "Throw away your magnifiers" As it's Facebook we can't really have too much writing in the image HOWEVER we want to highlight COMPLETE GLASSES $50 and that they will be the customers exact power lens. Our Website is www.lumaframe.com.au I have uploaded our logo but you do not need it in the design. We will be adding text to the Ad but not in the image you design (except for complete glasses for $50). you can take some of the images of frames from the website or I can upload just ask- tell me which one suits your design. Basically you have freedom to come up with something that will impress our potential customers make them click the link and check out our website.

Target Market(s)

People that use Cheap magnifiers - our glasses are a upgrade and better for their eyes

Industry/Entity Type

Eyewear

Colors

Designer to choose colors to be used in the design.

Requirements
Must have
• Complete Glasses $50 (Plus postage)- The (plus postage) in smaller writing than the Complete glasses for $50 part

```html
<!DOCTYPE html>
<html lang="en">
<head>
<meta charset="utf-8">
<title>Lumaframe — Complete Glasses $50</title>
<link href="https://fonts.googleapis.com/css2?family=Open+Sans:wght@600;700;800&display=swap" rel="stylesheet">
<style>
  :root {
    --paper: #ffffff;
    --panel-start: #2f86e0;
    --panel-end: #5a2ccb;
    --blob-blue: #3a8fe6;
    --blob-sky: #4aa6ec;
    --blob-violet: #5b2fd0;
    --blob-coral-start: #ff5a6e;
    --blob-coral-end: #e8346a;
    --text: #ffffff;
    --photo-hair: #6b5445;
    --photo-skin: #c9a48c;
    --photo-shirt: #f1f1f3;
  }
  html, body {
    margin: 0;
    padding: 0;
    overflow: hidden;
    background: var(--paper);
  }
  .ad {
    position: relative;
    width: 1200px;
    height: 628px;
    overflow: hidden;
    background: var(--paper);
    font-family: "Open Sans", Arial, sans-serif;
  }
  .layer {
    position: absolute;
    left: 0;
    top: 0;
  }
  .offer {
    position: absolute;
    left: 652px;
    top: 148px;
    width: 400px;
    text-align: center;
    color: var(--text);
  }
  .offer-line {
    margin: 0;
    font-weight: 700;
    font-size: 50px;
    line-height: 80px;
    letter-spacing: 1px;
  }
  .offer-price {
    margin: 8px 0 0;
    font-weight: 800;
    font-size: 124px;
    line-height: 132px;
    letter-spacing: -2px;
  }
  .offer-note {
    margin: 4px 0 0;
    font-weight: 600;
    font-size: 22px;
    line-height: 30px;
    letter-spacing: 1px;
  }
</style>
</head>
<body>
<div class="ad">
  <svg class="layer ad-backdrop" width="1200" height="628" viewBox="0 0 1200 628" aria-hidden="true">
    <defs>
      <linearGradient id="panelFill" x1="0" y1="0" x2="1" y2="0.4">
        <stop offset="0" stop-color="var(--panel-start)"/>
        <stop offset="1" stop-color="var(--panel-end)"/>
      </linearGradient>
      <linearGradient id="topLeftFill" x1="0" y1="1" x2="1" y2="0">
        <stop offset="0" stop-color="var(--blob-sky)"/>
        <stop offset="1" stop-color="var(--blob-violet)"/>
      </linearGradient>
      <linearGradient id="coralFill" x1="0" y1="0" x2="0" y2="1">
        <stop offset="0" stop-color="var(--blob-coral-start)"/>
        <stop offset="1" stop-color="var(--blob-coral-end)"/>
      </linearGradient>
    </defs>
    <rect class="panel" x="35" y="35" width="1130" height="543" fill="url(#panelFill)"/>
    <path class="blob blob-top-left" d="M0 0 H340 C330 40 290 60 240 60 C170 60 140 100 120 150 C95 210 40 190 0 180 Z" fill="url(#topLeftFill)"/>
    <path class="blob blob-top-right" d="M900 0 H1200 V270 C1175 250 1160 210 1150 160 C1138 100 1110 60 1060 45 C1000 30 940 30 900 0 Z" fill="var(--blob-blue)"/>
    <path class="blob blob-coral" d="M1200 330 C1150 335 1118 365 1112 420 C1105 480 1140 520 1140 570 C1140 600 1130 615 1125 628 H1200 Z" fill="url(#coralFill)"/>
    <g class="bubbles" fill="#ffffff">
      <circle cx="120" cy="130" r="45" opacity="0.3"/>
      <circle cx="55" cy="42" r="10" opacity="0.35"/>
      <circle cx="800" cy="78" r="7" opacity="0.35"/>
      <circle cx="1028" cy="68" r="11" opacity="0.35"/>
      <circle cx="1160" cy="132" r="18" opacity="0.3"/>
      <circle cx="997" cy="258" r="7" opacity="0.35"/>
      <circle cx="1160" cy="322" r="15" opacity="0.3"/>
      <circle cx="1110" cy="476" r="8" opacity="0.35"/>
      <circle cx="983" cy="521" r="9" opacity="0.35"/>
      <circle cx="765" cy="537" r="9" opacity="0.35"/>
    </g>
  </svg>

  <svg class="layer model-photo" width="1200" height="628" viewBox="0 0 1200 628" role="img" aria-label="Photo of a bearded man in large tortoiseshell glasses and a white patterned shirt, leaning forward with a surprised look">
    <defs>
      <linearGradient id="photoFill" x1="0" y1="0" x2="0" y2="1">
        <stop offset="0" stop-color="var(--photo-hair)"/>
        <stop offset="0.28" stop-color="var(--photo-skin)"/>
        <stop offset="0.5" stop-color="var(--photo-skin)"/>
        <stop offset="0.62" stop-color="var(--photo-shirt)"/>
        <stop offset="1" stop-color="var(--photo-shirt)"/>
      </linearGradient>
    </defs>
    <path d="M215 0 H470 C470 70 468 190 440 290 C500 308 565 335 612 385 C650 425 665 475 665 560 V628 H60 V470 C60 400 110 335 200 305 C240 292 258 282 265 272 C230 220 215 150 215 0 Z" fill="url(#photoFill)"/>
  </svg>

  <svg class="layer ad-front" width="1200" height="628" viewBox="0 0 1200 628" aria-hidden="true">
    <defs>
      <linearGradient id="bottomLeftFill" x1="0" y1="0" x2="1" y2="1">
        <stop offset="0" stop-color="var(--blob-sky)"/>
        <stop offset="1" stop-color="var(--blob-violet)"/>
      </linearGradient>
    </defs>
    <path class="blob blob-bottom-left" d="M0 400 C40 430 70 500 120 540 C180 590 260 560 330 570 C400 580 450 600 470 628 H0 Z" fill="url(#bottomLeftFill)"/>
    <circle cx="216" cy="543" r="8" fill="#ffffff" opacity="0.35"/>
  </svg>

  <div class="offer">
    <p class="offer-line">COMPLETE</p>
    <p class="offer-line">GLASSES</p>
    <p class="offer-price">-$50-</p>
    <p class="offer-note">(plus postage)</p>
  </div>
</div>
</body>
</html>
```